Redesign of existing bottle labels for gin, vodka and rum.

We are a small craft distillery with an existing range of spirits. We would like to "upgrade" our existing branding. Included in the attached file is the current artwork for the range we offer. We would like to retain the brand identity with the following enhancements in mind:
- More focus on the company logo.
- A single adhesion label with 3/4 wrap around and need to have external dimensions of 110mm high x 200mm wide.
- Also attached pictures of the existing bottles, we would like to retain the colored security seal with black top closure at the top. The newly design label should not conflict with this.
The new label should be clean lines and a minimalistic design.
Target Market(s)
Middle to high income professionals. Age group 18 to 65 years. Male and female.
Requirements
Must have
- Clean, minimalistic design
Nice to have
- Modern Feel
Should not have
- Cluttered Design

```html
<!DOCTYPE html>
<html lang="en">
<head>
<meta charset="utf-8">
<title>Kestrelvale Distillery – Cold-Distilled Gin Label</title>
<link rel="stylesheet" href="https://fonts.googleapis.com/css2?family=Montserrat:wght@500;600;700;800&display=swap">
<style>
  :root {
    --backdrop: #e9e9e7;
    --label-cream: #f4f0e0;
    --label-cream-light: #faf7ec;
    --ink: #161616;
    --copper: #c3875b;
    --seal-gold: #d99d26;
    --seal-gold-dark: #c88a17;
  }
  * { box-sizing: border-box; margin: 0; padding: 0; }
  html, body {
    width: 854px;
    height: 1200px;
    overflow: hidden;
    background: var(--backdrop);
  }
  .canvas {
    position: relative;
    width: 854px;
    height: 1200px;
  }
  .label {
    position: absolute;
    left: 18px;
    top: 238px;
    width: 818px;
    height: 724px;
    background: linear-gradient(90deg, var(--label-cream) 0%, var(--label-cream-light) 50%, var(--label-cream) 100%);
    font-family: "Montserrat", sans-serif;
    color: var(--ink);
    text-align: center;
  }
  .brand {
    position: absolute;
    top: 36px;
    left: 0;
    right: 0;
    display: flex;
    flex-direction: column;
    align-items: center;
  }
  .brand-mark {
    width: 170px;
    height: 170px;
  }
  .brand-name {
    margin-top: 14px;
    font-size: 40px;
    font-weight: 700;
    letter-spacing: 3px;
    line-height: 1;
    color: var(--ink);
  }
  .product-copy {
    position: absolute;
    top: 382px;
    left: 0;
    right: 0;
  }
  .product-title {
    font-size: 15px;
    font-weight: 800;
    letter-spacing: 0.5px;
    margin-bottom: 7px;
  }
  .product-story {
    font-size: 13px;
    font-weight: 500;
    line-height: 26px;
    letter-spacing: 0.4px;
    text-transform: uppercase;
  }
  .spirit-name {
    position: absolute;
    top: 500px;
    left: 0;
    right: 0;
    font-size: 88px;
    font-weight: 700;
    letter-spacing: 2px;
    line-height: 1;
  }
  .origin {
    position: absolute;
    top: 628px;
    left: 0;
    right: 0;
    font-size: 11.5px;
    font-weight: 600;
    letter-spacing: 1.6px;
    line-height: 26px;
    color: var(--copper);
    text-transform: uppercase;
  }
  .seal-band {
    position: absolute;
    left: 0;
    right: 0;
    bottom: 6px;
    height: 22px;
    background: linear-gradient(180deg, var(--seal-gold) 0%, var(--seal-gold-dark) 100%);
  }
</style>
</head>
<body>
  <main class="canvas">
    <section class="label" aria-label="Kestrelvale Distillery gin label">
      <header class="brand">
        <svg class="brand-mark" viewBox="0 0 170 170" aria-hidden="true">
          <circle cx="85" cy="85" r="80" fill="none" stroke="#161616" stroke-width="5"/>
        </svg>
        <p class="brand-name">KESTRELVALE DISTILLERY</p>
      </header>

      <div class="product-copy">
        <h2 class="product-title">COLD-DISTILLED GIN</h2>
        <p class="product-story">
          Our handcrafted, small-batch, cold-distilled gin brings<br>
          tofether purpose-built equipment, the purest ingredients, finestbotanicals<br>
          and passion to produce an unmatched gin worthy of your company
        </p>
      </div>

      <h1 class="spirit-name">GIN</h1>

      <p class="origin">
        Distilled &amp; bottled in South Africa<br>
        by Kestrelvale Distillery
      </p>

      <div class="seal-band"></div>
    </section>
  </main>
</body>
</html>
```